Lena Corvell Business Card

I need a business card that reflects my current website: itslenacorvell.example and screenshot attached. If we keep the color scheme of the site and sample card below that would be ideal. The business card should include the information on the attached sample cards.

Industry/Entity Type

Business

```html
<!DOCTYPE html>
<html lang="en">
<head>
<meta charset="utf-8">
<title>Lena Corvell Business Card</title>
<link rel="stylesheet" href="https://fonts.googleapis.com/css2?family=Didact+Gothic&display=swap">
<style>
  :root {
    --page-bg: #eef1f0;
    --teal: #5cbfaa;
    --teal-light: #6ccab7;
    --teal-deep: #4fb29d;
    --pattern-tone: #52b39f;
    --ink: #ffffff;
    --ink-soft: rgba(255, 255, 255, 0.9);
    --card-shadow: rgba(30, 60, 55, 0.18);
  }
  * { box-sizing: border-box; margin: 0; padding: 0; }
  html, body {
    width: 1200px;
    height: 900px;
    overflow: hidden;
    background: var(--page-bg);
    font-family: "Didact Gothic", "Century Gothic", sans-serif;
  }
  .canvas {
    width: 1200px;
    height: 900px;
    display: flex;
    flex-direction: column;
    align-items: center;
    justify-content: center;
    gap: 60px;
  }
  .card {
    position: relative;
    width: 630px;
    height: 360px;
    border-radius: 4px;
    overflow: hidden;
    box-shadow: 0 8px 24px var(--card-shadow);
    color: var(--ink);
  }
  .card-front { background: var(--teal); }
  .name-pattern {
    position: absolute;
    inset: 0;
    background: linear-gradient(160deg, var(--teal) 0%, var(--pattern-tone) 50%, var(--teal) 100%);
  }
  .front-wordmark {
    position: absolute;
    left: 0; right: 0; top: 50%;
    transform: translateY(-50%);
    text-align: center;
    font-size: 36px;
    letter-spacing: 1px;
    color: var(--ink);
  }
  .card-back {
    background: linear-gradient(170deg, var(--teal-light) 0%, var(--teal) 55%, var(--teal-deep) 100%);
    display: flex;
    flex-direction: column;
    align-items: center;
    justify-content: center;
    text-align: center;
  }
  .holder-name {
    font-size: 38px;
    letter-spacing: 1px;
    margin-bottom: 10px;
  }
  .holder-roles {
    font-size: 13px;
    letter-spacing: 0.4px;
    color: var(--ink-soft);
    margin-bottom: 30px;
  }
  .contact-list {
    list-style: none;
    font-size: 13px;
    line-height: 1.75;
    color: var(--ink-soft);
    letter-spacing: 0.3px;
  }
  .contact-social {
    display: inline-flex;
    align-items: center;
    gap: 6px;
  }
  .social-dot {
    width: 7px; height: 7px;
    border-radius: 50%;
    background: var(--ink-soft);
  }
</style>
</head>
<body>
  <main class="canvas">
    <section class="card card-front">
      <div class="name-pattern" role="img" aria-label="Faint repeated hand-lettered name pattern in deeper teal"></div>
      <p class="front-wordmark">Lena Corvell</p>
    </section>

    <section class="card card-back">
      <h1 class="holder-name">Lena Corvell</h1>
      <p class="holder-roles">Brand Curator | Digital Storyteller | Social Entrepreneur</p>
      <ul class="contact-list">
        <li>me@lenacorvell.example</li>
        <li>555.010.4821</li>
        <li><span class="contact-social"><span class="social-dot"></span>@itslenacorvell</span></li>
        <li>www.itslenacorvell.example</li>
      </ul>
    </section>
  </main>
</body>
</html>
```